Corvalen Capital Modern Business Card

We need a modern business card template designed for Corvalen Capital.
Corvalen Capital is a diversified global cryptocurrency investment fund.

The font under the logo: Hiragino Kaku Gothic Pro

Color Hexcode: Main colors white (ffffff) & teal (188383), we are open to adding #fcca46 as an accent

Need time to get feedback from my team and to make sure designers better understand the brief.

Target Market(s)

Accredited Investors, high net worth individuals and institutional investors

Industry/Entity Type

Investment

Contact Information for Business Card

Contact Information should contain
Name
main phone +1 720 555 0147
cell
email

Font styles to use
Sans Serif
Other font styles liked:
• Hiragino Kaku Gothic Pro

Requirements
Must have
• would like to have icons that identify the contact information
• include our website: www.corvalencapital.example
• include our Tagline: Diversified Crypto Investment Funds
Nice to have
• Would like to have a simple back side with the logo (without the words) and plenty of space

```html
<!DOCTYPE html>
<html lang="en">
<head>
<meta charset="utf-8">
<title>Corvalen Capital Business Card</title>
<link rel="stylesheet" href="https://fonts.googleapis.com/css2?family=Roboto:wght@400;500&family=Roboto+Condensed:wght@500;700&display=swap">
<style>
  :root {
    --backdrop: #2b2b2b;
    --card: #f4f4f4;
    --teal: #1d9494;
    --ink: #1a1a1a;
    --text: #4a4a4a;
    --white: #ffffff;
    --pattern-a: #eef3f3;
    --pattern-b: #e4eded;
  }
  * { margin: 0; padding: 0; box-sizing: border-box; }
  html, body {
    width: 1200px; height: 960px; overflow: hidden;
    background: var(--backdrop);
    font-family: "Roboto", sans-serif;
  }
  .canvas { position: relative; width: 1200px; height: 960px; }
  .card {
    position: absolute; width: 600px; height: 343px;
    background: var(--card); overflow: hidden;
  }
  .card-front { left: 314px; top: 113px; }
  .card-back { left: 311px; top: 472px; }

  .brand {
    position: absolute; left: 30px; top: 150px;
    display: flex; align-items: center; gap: 10px;
  }
  .brand-square { width: 16px; height: 16px; background: var(--teal); }
  .brand-name {
    font-family: "Roboto", sans-serif; font-weight: 400;
    font-size: 20px; letter-spacing: 0.3px; color: var(--ink);
    text-transform: uppercase;
  }
  .divider-band { position: absolute; left: 0; top: 132px; }
  .person {
    position: absolute; right: 35px; top: 137px; text-align: right;
    font-family: "Roboto Condensed", sans-serif; color: var(--white);
    text-transform: uppercase;
  }
  .person-name { font-weight: 700; font-size: 22px; line-height: 26px; }
  .person-role { font-weight: 500; font-size: 15px; line-height: 20px; letter-spacing: 0.3px; }

  .contacts { position: absolute; left: 30px; top: 223px; list-style: none; }
  .contact {
    display: flex; align-items: center; gap: 8px;
    font-size: 14px; line-height: 19px; color: var(--text);
  }
  .contact svg { width: 14px; height: 14px; fill: var(--teal); flex: none; }
  .tagline {
    position: absolute; left: 29px; top: 304px;
    font-weight: 500; font-size: 14px; color: var(--text);
  }

  .back-pattern {
    position: absolute; inset: 0;
    background: linear-gradient(180deg, var(--pattern-a), var(--pattern-b));
  }
  .back-brand {
    position: absolute; right: 50px; bottom: 50px;
    display: flex; align-items: center; gap: 8px;
  }
  .back-brand .brand-name { font-size: 16px; color: var(--teal); }
</style>
</head>
<body>
<main class="canvas">
  <section class="card card-front">
    <div class="brand">
      <span class="brand-square"></span>
      <span class="brand-name">Corvalen Capital</span>
    </div>
    <svg class="divider-band" width="600" height="56" viewBox="0 0 600 56">
      <line x1="0" y1="54.5" x2="350" y2="54.5" stroke="var(--teal)" stroke-width="1"/>
      <polygon points="346,55 385,0 600,0 600,55" fill="var(--teal)"/>
    </svg>
    <div class="person">
      <div class="person-name">Dorian Maleko</div>
      <div class="person-role">Co-Founder</div>
    </div>
    <ul class="contacts">
      <li class="contact">
        <svg viewBox="0 0 24 24"><path d="M6.6 10.8a15.1 15.1 0 0 0 6.6 6.6l2.2-2.2c.3-.3.7-.4 1-.2 1.1.4 2.3.6 3.6.6.6 0 1 .4 1 1V20c0 .6-.4 1-1 1A17 17 0 0 1 3 4c0-.6.4-1 1-1h3.5c.6 0 1 .4 1 1 0 1.3.2 2.5.6 3.6.1.3 0 .7-.2 1z"/></svg>
        <span>+1 720 555 0147</span>
      </li>
      <li class="contact">
        <svg viewBox="0 0 24 24"><path d="M7 1h10a2 2 0 0 1 2 2v18a2 2 0 0 1-2 2H7a2 2 0 0 1-2-2V3a2 2 0 0 1 2-2zm0 3v14h10V4zm5 15.5a1 1 0 1 0 0 2 1 1 0 0 0 0-2z"/></svg>
        <span>+1 720 555 0182</span>
      </li>
      <li class="contact">
        <svg viewBox="0 0 24 24"><path d="M2 5h20v14H2zm2 2v.5l8 5 8-5V7zm0 3v7h16v-7l-8 5z"/></svg>
        <span>dorian@corvalencapital.example</span>
      </li>
      <li class="contact">
        <svg viewBox="0 0 24 24"><path d="M12 2a10 10 0 1 0 0 20 10 10 0 0 0 0-20zm-1 17.9A8 8 0 0 1 4.2 10.6L9 15.4v1a2 2 0 0 0 2 2zm6.9-2.5A2 2 0 0 0 16 16h-1v-3a1 1 0 0 0-1-1H8v-2h2a1 1 0 0 0 1-1V7h2a2 2 0 0 0 2-2v-.4a8 8 0 0 1 2.9 12.8z"/></svg>
        <span>www.corvalencapital.example</span>
      </li>
    </ul>
    <p class="tagline">Diversified Crypto Investment Funds</p>
  </section>

  <section class="card card-back">
    <div class="back-pattern" role="img" aria-label="Faint light teal repeating geometric background pattern"></div>
    <div class="back-brand">
      <span class="brand-square"></span>
      <span class="brand-name">Corvalen Capital</span>
    </div>
  </section>
</main>
</body>
</html>
```